Moving Company Needs Business Card Design

We need a business cars for moving company based in San Diego. We are called Harborline Moving Systems. We move locally and long distance. 1st side: Logo, website: www.HarborlineMoving.example, Telephone number: 1-855-314-7086.
2nd side: Licensed and Insured,
We move homes and businesses
Services: Local Moving, Long Distance Moving, Loading / Unloading your truck / container, On-site Moving, Packing Service
telephone number 1-855-314-7086, email: info@harborlinemoving.example

```html
<!DOCTYPE html>
<html lang="en">
<head>
<meta charset="utf-8">
<title>Harborline Moving Systems – Business Card</title>
<link href="https://fonts.googleapis.com/css2?family=Exo+2:wght@400;600;800&display=swap" rel="stylesheet">
<style>
  :root {
    --brand-red: #d7141d;
    --brand-red-deep: #a50d14;
    --brand-navy: #1b2f7a;
    --card-white: #ffffff;
    --card-shade: #eceef0;
    --ink-grey: #4a4d52;
    --page-bg: #e4e6e9;
  }
  * { box-sizing: border-box; margin: 0; padding: 0; }
  html, body { width: 1200px; height: 900px; overflow: hidden; }
  body {
    background: var(--page-bg);
    font-family: "Exo 2", sans-serif;
    display: flex;
    align-items: center;
    justify-content: space-evenly;
  }
  .card {
    position: relative;
    width: 540px;
    height: 320px;
    border-radius: 28px;
    overflow: hidden;
    background: linear-gradient(180deg, var(--card-white) 0%, var(--card-shade) 100%);
    box-shadow: 0 10px 28px rgba(0,0,0,0.18);
  }
  .card-wave { position: absolute; inset: 0; width: 100%; height: 100%; }
  .brand-name {
    position: absolute;
    color: var(--brand-red);
    font-weight: 800;
    text-transform: uppercase;
    line-height: 1;
  }
  .card-front .brand-name { left: 34px; top: 30px; font-size: 22px; letter-spacing: 0.5px; }
  .brand-name small { display: block; font-size: 0.55em; letter-spacing: 2px; margin-top: 5px; }
  .holder {
    position: absolute;
    right: 40px;
    top: 52px;
    text-align: right;
    color: var(--ink-grey);
    text-transform: uppercase;
  }
  .holder-name { font-size: 20px; font-weight: 600; letter-spacing: 1px; }
  .holder-role { font-size: 12px; font-weight: 400; letter-spacing: 1.5px; margin-top: 4px; }
  .address {
    position: absolute;
    left: 30px;
    top: 162px;
    color: var(--card-white);
    font-size: 13px;
    line-height: 1.45;
    font-weight: 400;
    font-style: normal;
  }
  .contacts {
    position: absolute;
    right: 26px;
    top: 172px;
    list-style: none;
    color: var(--card-white);
    font-size: 12.5px;
    text-align: right;
  }
  .contacts li {
    display: flex;
    align-items: center;
    justify-content: flex-end;
    gap: 8px;
    height: 24px;
  }
  .contacts svg { width: 13px; height: 13px; fill: var(--card-white); flex: none; }

  .card-back {
    display: flex;
    flex-direction: column;
    align-items: center;
    justify-content: center;
    gap: 14px;
    padding: 26px 34px;
    text-align: center;
  }
  .card-back .brand-name { position: static; font-size: 32px; letter-spacing: 1px; }
  .back-tagline {
    color: var(--brand-navy);
    font-size: 13px;
    font-weight: 600;
    letter-spacing: 1.2px;
    text-transform: uppercase;
  }
  .back-tagline span { color: var(--brand-red); margin: 0 6px; }
  .services {
    list-style: none;
    display: grid;
    grid-template-columns: auto auto;
    column-gap: 22px;
    row-gap: 3px;
    color: var(--ink-grey);
    font-size: 12.5px;
    text-align: left;
  }
  .services li::before { content: "•"; color: var(--brand-red); margin-right: 6px; }
  .services .wide { grid-column: 1 / -1; }
  .back-contacts {
    display: flex;
    gap: 22px;
    color: var(--brand-navy);
    font-size: 12.5px;
    font-weight: 600;
  }
</style>
</head>
<body>
  <section class="card card-front" aria-label="Business card front">
    <svg class="card-wave" viewBox="0 0 540 320" preserveAspectRatio="none" aria-hidden="true">
      <defs>
        <linearGradient id="redBand" x1="0" y1="0" x2="1" y2="1">
          <stop offset="0" stop-color="#e51b24"/>
          <stop offset="1" stop-color="#a50d14"/>
        </linearGradient>
      </defs>
      <path d="M0,140 C220,108 440,100 540,150 L540,320 L0,320 Z" fill="url(#redBand)"/>
      <path d="M0,134 C220,98 440,88 540,140 L540,152 C440,104 220,112 0,142 Z" fill="var(--brand-navy)"/>
    </svg>

    <div class="brand-name">Harborline<small>Moving Systems</small></div>

    <div class="holder">
      <div class="holder-name">Daniel Reyes</div>
      <div class="holder-role">Financial Advisor</div>
    </div>

    <address class="address">
      27 Harbor Street, Suite 4<br>Bayview Road SD
    </address>

    <ul class="contacts">
      <li>1-855-314-7086
        <svg viewBox="0 0 16 16"><path d="M3 1l3 3-1.5 2a9 9 0 005.5 5.5L12 10l3 3-2 2C7 15 1 9 1 3z"/></svg>
      </li>
      <li>1-855-314-7086
        <svg viewBox="0 0 16 16"><path d="M2 2h12v12H2z M4 4v8h8V4z M5 6h6v1H5z M5 8h6v1H5z"/></svg>
      </li>
      <li>1-855-314-7086
        <svg viewBox="0 0 16 16"><path d="M4 1h8a1 1 0 011 1v12a1 1 0 01-1 1H4a1 1 0 01-1-1V2a1 1 0 011-1zm1 2v9h6V3z"/></svg>
      </li>
      <li>info@harborlinemoving.example
        <svg viewBox="0 0 16 16"><path d="M1 3h14v10H1z M2 4l6 5 6-5z" fill-rule="evenodd"/></svg>
      </li>
      <li>www.HarborlineMoving.example
        <svg viewBox="0 0 16 16"><circle cx="8" cy="8" r="6.5" fill="none" stroke="#fff" stroke-width="1.3"/><path d="M1.5 8h13M8 1.5v13" stroke="#fff" stroke-width="1"/></svg>
      </li>
    </ul>
  </section>

  <section class="card card-back" aria-label="Business card back">
    <div class="brand-name">Harborline<small>Moving Systems</small></div>
    <p class="back-tagline">Licensed and Insured<span>|</span>We move homes and businesses</p>
    <ul class="services">
      <li>Local Moving</li>
      <li>Long Distance Moving</li>
      <li class="wide">Loading / Unloading your truck / container</li>
      <li>On-site Moving</li>
      <li>Packing Service</li>
    </ul>
    <p class="back-contacts"><span>1-855-314-7086</span><span>info@harborlinemoving.example</span></p>
  </section>
</body>
</html>
```